VELDA Medical Spa

We'd like a business card with the reverse of the card for appointments. We like round corners and vertical design. We have a background image and bird logo to include with the following wording on the front:-
Velda Medical Spa
58 Brackley Street
NORTH ADELAIDE
SA 5006
Phone 08 83914076
www.veldamedicalspa.com.au
Facebook veldamedicalspa
Instagram veldamedicalspa
On the back I'd like an appointment card layout please.
Cheers Dot

```html
<!DOCTYPE html>
<html lang="en">
<head>
<meta charset="utf-8">
<title>VELDA Medical Spa – Business &amp; Appointment Card</title>
<link rel="stylesheet" href="https://fonts.googleapis.com/css2?family=EB+Garamond:wght@400;500&family=Alegreya:wght@500&display=swap">
<style>
  :root {
    --stage: #3b3b3d;
    --mint-light: #d6f0e2;
    --mint: #a9e0d0;
    --teal-soft: #7fcdc9;
    --ink: #2f3433;
    --sage: #9ccbae;
    --teal-text: #5aa39a;
    --paper: #ffffff;
    --dots: #7a7a7a;
  }
  * { box-sizing: border-box; margin: 0; padding: 0; }
  html, body { width: 1200px; height: 900px; overflow: hidden; }
  body {
    background: var(--stage);
    font-family: "EB Garamond", Georgia, serif;
    color: var(--ink);
    position: relative;
  }
  .card {
    position: absolute;
    top: 70px;
    width: 434px;
    height: 760px;
    border-radius: 28px;
    overflow: hidden;
  }
  .card--front { left: 136px; }
  .card--back { left: 630px; background: var(--paper); }

  .front-backdrop {
    position: absolute; inset: 0;
    background:
      radial-gradient(ellipse at 80% 70%, var(--teal-soft) 0%, rgba(127,205,201,0) 60%),
      linear-gradient(160deg, var(--mint-light) 0%, var(--mint) 55%, var(--teal-soft) 100%);
  }
  .front-content {
    position: relative;
    height: 100%;
    display: flex; flex-direction: column; align-items: center;
    padding-top: 170px;
    text-align: center;
  }
  .brand-name {
    font-family: "EB Garamond", Georgia, serif;
    font-weight: 400;
    font-size: 40px;
    line-height: 1;
    color: var(--ink);
  }
  .brand-rule {
    width: 130px; height: 1px; background: var(--ink);
    margin: 52px 0 30px;
  }
  .spa-name {
    font-size: 26px; letter-spacing: 1px; text-transform: uppercase;
  }
  .contact-icons { display: flex; gap: 8px; margin: 18px 0 14px; }
  .contact-icons svg { width: 26px; height: 26px; }
  .contact-line { font-size: 21px; line-height: 1.25; }
  .address { margin-top: 14px; font-size: 21px; line-height: 1.15; }
  .follow {
    margin-top: 26px;
    display: flex; align-items: center; gap: 12px;
    width: 340px; font-size: 24px;
  }
  .follow::before, .follow::after {
    content: ""; flex: 1; height: 1px; background: var(--ink);
  }
  .social { display: flex; align-items: center; gap: 8px; margin-top: 10px; font-size: 22px; }
  .social-square { width: 22px; height: 22px; border-radius: 4px; }
  .social-square--one { background: #6d7fc4; }
  .social-square--two { background: #d95a8a; }
  .social-handle { margin-left: 8px; }

  .back-content {
    height: 100%;
    display: flex; flex-direction: column; align-items: center;
    padding: 40px 44px 0;
  }
  .back-badge {
    width: 250px; height: 250px; border-radius: 50%;
    background: var(--sage);
  }
  .back-name {
    margin-top: 14px;
    font-size: 28px;
    color: var(--ink);
  }
  .appointment-title {
    font-family: "Alegreya", Georgia, serif;
    font-weight: 500;
    color: var(--teal-text);
    font-size: 30px; letter-spacing: 2px;
    margin: 18px 0 28px;
  }
  .field-list { width: 100%; list-style: none; }
  .field {
    display: flex; align-items: flex-end; gap: 8px;
    font-size: 22px; height: 50px;
  }
  .field-line { flex: 1; border-bottom: 1px dotted var(--dots); margin-bottom: 6px; }
  .field-suffix { font-size: 19px; }
  .appointment-note {
    margin-top: auto; margin-bottom: 48px;
    text-align: center; font-size: 20px; line-height: 1.25;
  }
</style>
</head>
<body>
  <section class="card card--front">
    <div class="front-backdrop" role="img" aria-label="Soft mint and teal background photo of palm fronds"></div>
    <div class="front-content">
      <div class="brand-name">VELDA</div>
      <div class="brand-rule"></div>
      <div class="spa-name">VELDA Medical Spa</div>
      <div class="contact-icons">
        <svg viewBox="0 0 26 26" aria-label="phone"><rect width="26" height="26" rx="5" fill="#2f3433"/><path d="M8 7c1-1 2-1 3 0l1 2-2 2c1 2 2 3 4 4l2-2 2 1c1 1 1 2 0 3-3 2-11-6-10-10z" fill="#a9e0d0"/></svg>
        <svg viewBox="0 0 26 26" aria-label="website"><rect width="26" height="26" rx="5" fill="#2f3433"/><circle cx="13" cy="13" r="7" fill="none" stroke="#a9e0d0" stroke-width="1.6"/><path d="M6 13h14M13 6c-3 4-3 10 0 14M13 6c3 4 3 10 0 14" fill="none" stroke="#a9e0d0" stroke-width="1.4"/></svg>
        <svg viewBox="0 0 26 26" aria-label="location"><rect width="26" height="26" rx="5" fill="#2f3433"/><path d="M13 5a6 6 0 0 1 6 6c0 4-6 10-6 10s-6-6-6-10a6 6 0 0 1 6-6z" fill="#a9e0d0"/><circle cx="13" cy="11" r="2.2" fill="#2f3433"/></svg>
      </div>
      <div class="contact-line">08 83914076</div>
      <div class="contact-line">www.veldamedicalspa.com.au</div>
      <div class="address">58 Brackley Street<br>NORTH ADELAIDE<br>SA 5006</div>
      <div class="follow">follow us on</div>
      <div class="social">
        <span class="social-square social-square--one"></span>
        <span class="social-square social-square--two"></span>
        <span class="social-handle">@ veldamedicalspa</span>
      </div>
    </div>
  </section>

  <section class="card card--back">
    <div class="back-content">
      <div class="back-badge"></div>
      <div class="back-name">VELDA</div>
      <h2 class="appointment-title">Next Appointment</h2>
      <ul class="field-list">
        <li class="field"><span class="field-label">Name</span><span class="field-line"></span></li>
        <li class="field"><span class="field-label">Date</span><span class="field-line"></span><span class="field-suffix">am/pm</span></li>
        <li class="field"><span class="field-label">Time</span><span class="field-line"></span></li>
        <li class="field"><span class="field-label">Note</span><span class="field-line"></span></li>
        <li class="field"><span class="field-line"></span></li>
      </ul>
      <p class="appointment-note">If unable to keep the Appointment<br>Or For Any Question Please Call Us</p>
    </div>
  </section>
</body>
</html>
```